Website Redesign for Existing BBQ Catering Company

Need to get my website (Brindlewick.com) redesigned. Looking for a cleaner look but still patriotic and rustic. Would like to add parallax scrolling on the menu page and include some pics from our photo gallery. Would like to display a picture of the brisket before scrolling into the meat section of our menu and the same for the other sections too.....picture of one of our sides, appetizers, desserts, etc.

Would also like to add three new pages called Corporate Events, Weddings, and Veteran Events possibly in a drop-down menu called Catering. You can use pics from our Facebook page. We've posted tons of pics from weddings that we've done. I've uploaded some corporate and wedding pics but you can pics the ones that look best. I can swap them out later if needed.

Would like to keep it Wordpress if possible so I can update it as needed.

Also need to add some links to our storefront on The Velvet Ledger. I have the HTML code and will upload the image here.

Also need to add social media links for our Facebook, Instagram and Twitter pages.

The contact form that I'm using now feeds the leads into another site called Quillora.com that I use to manage my clients.

Target Market(s)

Weddings, corporate events, veterans

Industry/Entity Type

Catering

Coding

Coded - Design and coding required

Number of Pages Required

5+ page

Colors
ec1f27
3176b5
ffffff

Requirements
Must have
• Really like the hero image design. Looks less like a template. Check out https://vantelo.com and https://amberlinocrest.com
• Would like to keep somewhat of a rustic and patriotic look and feel like the site currently is. We mainly cater in barn weddings and we cater for a lot of veterans. Will be pushing more corporate catering next year and opening a restaurant.

```html
<!DOCTYPE html>
<html lang="en">
<head>
<meta charset="utf-8">
<title>Brindlewick BBQ — Premium Quality Barbeque</title>
<link rel="stylesheet" href="https://fonts.googleapis.com/css2?family=Alfa+Slab+One&family=Montserrat:wght@500&family=Permanent+Marker&family=Stardos+Stencil:wght@700&display=swap">
<style>
  :root {
    --wood-dark: #2a110a;
    --wood-seam: #1e0b06;
    --wood-mid: #4a2013;
    --wood-light: #5e2b19;
    --wood-edge: #7a3d24;
    --cream: #f4ecdc;
    --white-soft: #e6e4e2;
    --brand-red: #ec1f27;
    --brand-blue: #3176b5;
    --brand-white: #ffffff;
    --meat-dark: #1a0d0a;
    --meat-mid: #4e2c24;
    --meat-warm: #74402a;
    --board-light: #8d7f78;
    --amber: #8a5a2a;
  }
  * { box-sizing: border-box; margin: 0; padding: 0; }
  html, body { width: 1200px; height: 568px; overflow: hidden; background: var(--meat-dark); }
  .page { position: relative; width: 1200px; height: 568px; display: flex; }

  .sidebar {
    position: relative;
    width: 220px;
    height: 568px;
    border-right: 2px solid var(--wood-edge);
    text-align: center;
    color: var(--cream);
  }
  .sidebar-wood {
    position: absolute; inset: 0;
    background:
      repeating-linear-gradient(90deg,
        transparent 0, transparent 31px,
        var(--wood-seam) 31px, var(--wood-seam) 33px,
        transparent 33px, transparent 34px),
      repeating-linear-gradient(90deg,
        rgba(255,255,255,0.03) 0, rgba(0,0,0,0.06) 9px,
        rgba(255,255,255,0.02) 17px, rgba(0,0,0,0.05) 26px, rgba(255,255,255,0.03) 34px),
      radial-gradient(ellipse at 50% 30%, var(--wood-light) 0%, var(--wood-mid) 55%, var(--wood-dark) 100%);
  }
  .sidebar-content { position: relative; }

  .brand {
    position: absolute; left: 0; top: 20px; width: 220px;
    display: flex; flex-direction: column; align-items: center; gap: 7px;
  }
  .brand-mark {
    width: 100px; height: 100px; border-radius: 50%;
    background: var(--brand-blue);
    border: 5px solid var(--brand-white);
    box-shadow: 0 0 0 4px var(--brand-red);
  }
  .brand-name {
    font-family: "Alfa Slab One", serif;
    font-size: 13px; letter-spacing: 0.5px;
    color: var(--cream);
  }

  .main-nav {
    position: absolute; left: 0; top: 156px; width: 220px;
    list-style: none;
  }
  .main-nav li {
    font-family: "Alfa Slab One", serif;
    font-size: 14.5px; line-height: 27.2px;
    letter-spacing: 0.4px;
    color: var(--cream);
  }

  .divider {
    position: absolute; left: 35px; top: 338px;
    width: 140px; height: 1px; background: var(--cream); opacity: 0.85;
  }

  .contact {
    position: absolute; left: 0; top: 347px; width: 220px;
    font-family: "Montserrat", sans-serif; font-weight: 500;
    font-size: 10px; line-height: 12px; color: var(--cream);
    font-style: normal;
  }

  .social {
    position: absolute; left: 0; top: 420px; width: 220px;
    display: flex; justify-content: center; gap: 8px;
    list-style: none;
  }
  .social li { width: 11px; height: 11px; border-radius: 50%; background: var(--cream); }

  .hero { position: relative; flex: 1; height: 568px; overflow: hidden; }
  .hero-photo {
    position: absolute; inset: 0;
    background:
      radial-gradient(ellipse 30% 40% at 92% 15%, #0e0a0a 0%, transparent 100%),
      radial-gradient(ellipse 35% 30% at 30% 8%, var(--board-light) 0%, transparent 100%),
      radial-gradient(ellipse 30% 35% at 85% 85%, var(--amber) 0%, transparent 100%),
      radial-gradient(ellipse 45% 40% at 55% 30%, var(--meat-warm) 0%, transparent 100%),
      radial-gradient(ellipse 50% 55% at 15% 70%, #6a3a30 0%, transparent 100%),
      linear-gradient(150deg, var(--meat-mid) 0%, #2e1813 50%, #3d2418 100%);
  }
  .hero-shade { position: absolute; inset: 0; background: rgba(0,0,0,0.22); }

  .hero-tagline {
    position: absolute; left: 178px; top: 226px; width: 660px;
    font-family: "Permanent Marker", cursive;
    font-size: 26px; letter-spacing: 0.5px; word-spacing: 3px;
    color: var(--white-soft); white-space: nowrap;
  }
  .hero-title {
    position: absolute; left: 176px; top: 258px; width: 660px;
    font-family: "Stardos Stencil", serif; font-weight: 700;
    font-size: 123px; line-height: 1.1;
    letter-spacing: -1px;
    color: var(--white-soft); white-space: nowrap;
  }
</style>
</head>
<body>
<div class="page">
  <aside class="sidebar">
    <div class="sidebar-wood" role="img" aria-label="Dark rustic barn wood plank background"></div>
    <div class="sidebar-content">
      <div class="brand">
        <span class="brand-mark"></span>
        <span class="brand-name">BRINDLEWICK BBQ</span>
      </div>
      <ul class="main-nav">
        <li>CORPORATE</li>
        <li>WEDDINGS</li>
        <li>VETERAN</li>
        <li>MENU</li>
        <li>GALLERY</li>
        <li>CONTACT US</li>
      </ul>
      <div class="divider"></div>
      <address class="contact">
        88 Harrow Lane #100<br>
        Fenmoor, CA 95970<br>
        555-014-2290<br>
        contact@brindlewick.com
      </address>
      <ul class="social" aria-label="Social links">
        <li></li><li></li><li></li><li></li>
      </ul>
    </div>
  </aside>

  <main class="hero">
    <div class="hero-photo" role="img" aria-label="Close-up of sliced smoked brisket with dark bark on a cutting board, knife and gloved hand"></div>
    <div class="hero-shade"></div>
    <p class="hero-tagline">PREMIUM QUALITY .&nbsp; SMOKED SLOW &amp; LOW</p>
    <h1 class="hero-title">BARBEQUE</h1>
  </main>
</div>
</body>
</html>
```